OSB - Brochure 52 week Curriculum

Oakstone Brotherhood, Inc. wants to create a distribution Brochure. In the Bible (Matthew 28:18-20)- JESUS said to "TEACH" others what HE has commanded. we want to "PUT IN PRINT"

these 52 lines summarize HIS teachings
we want to use as our Curriculum teaching men ...

incorporate our statements and two main passages of scripture
(see attach pictures of headquarter lobby) to brand uniformity and consistency... we have summarized into 52 groups, but its NOT required to have numbers...
Purpose = obey GOD
Mission = love others
Vision = Development God fearing men globally.

The designer can have freedom in layout and sizing.
we were thinking bi fold , but again... designer has freedom
Please incorporate our colors (white, black, gray) using color wheel provided and our LOGO with website.

```html
<!DOCTYPE html>
<html lang="en">
<head>
<meta charset="UTF-8">
<title>Oakstone Brotherhood – Teachings of Jesus Brochure</title>
<link href="https://fonts.googleapis.com/css2?family=Montserrat:ital,wght@0,400;0,500;0,700;0,800;1,400&display=swap" rel="stylesheet">
<style>
  :root {
    --backdrop: #8f6a16;
    --page-white: #ececec;
    --page-gold: #d9b35a;
    --gold-light: #f1dc95;
    --gold-deep: #c2913a;
    --ink: #1c1c1e;
    --ink-soft: #3a3a3c;
    --rule: #2a2a2a;
  }
  * { box-sizing: border-box; margin: 0; padding: 0; }
  html, body { width: 1200px; height: 840px; overflow: hidden; }
  body {
    background: var(--backdrop);
    font-family: "Montserrat", Arial, sans-serif;
    color: var(--ink);
  }
  .spread {
    position: absolute;
    left: 80px; top: 52px;
    width: 1040px; height: 736px;
    display: flex;
  }
  .page {
    position: relative;
    width: 520px; height: 736px;
    overflow: hidden;
  }
  .page--inside { background: var(--page-white); padding: 70px 52px 0; }
  .page--cover { background: var(--page-gold); }

  .brand { text-align: center; }
  .brand__name {
    font-weight: 800;
    font-size: 78px;
    line-height: 1;
    letter-spacing: 2px;
    color: var(--ink);
  }
  .brand__url {
    font-weight: 700;
    font-size: 11px;
    letter-spacing: 1px;
    margin-top: 6px;
    text-transform: uppercase;
  }

  .pillars {
    display: flex;
    align-items: flex-start;
    margin-top: 56px;
    gap: 18px;
  }
  .pillar__title { font-weight: 700; font-size: 27px; line-height: 1.05; }
  .pillar__label { font-weight: 700; font-size: 10px; margin-top: 3px; }
  .pillars__divider { width: 2px; height: 44px; background: var(--rule); margin-top: 2px; }

  .verse {
    font-size: 9.5px;
    line-height: 1.55;
    color: var(--ink-soft);
    margin-top: 16px;
    text-align: justify;
  }
  .verse__ref {
    font-style: italic;
    font-size: 9px;
    text-align: right;
    margin-top: 10px;
  }
  .vision { margin-top: 40px; }
  .vision__title { font-weight: 700; font-size: 30px; line-height: 1.05; }
  .vision__label { font-weight: 700; font-size: 12px; margin-top: 4px; }

  .cover__scene {
    position: absolute;
    left: 0; top: 0;
    width: 520px; height: 440px;
    background:
      radial-gradient(ellipse at 78% 40%, #fff4c4 0%, rgba(241,220,149,0.6) 30%, rgba(217,179,90,0) 65%),
      linear-gradient(180deg, var(--gold-light) 0%, #e6c073 55%, var(--page-gold) 100%);
  }
  .cover__scene::after {
    content: "";
    position: absolute; left: 0; right: 0; bottom: 0; height: 120px;
    background: linear-gradient(180deg, rgba(217,179,90,0), var(--page-gold));
  }
  .cover__title {
    position: absolute;
    left: 60px; top: 430px;
    font-weight: 800;
    line-height: 0.95;
  }
  .cover__title-top { font-size: 44px; letter-spacing: 1px; display: block; }
  .cover__title-of { font-size: 26px; }
  .cover__title-main { font-size: 72px; letter-spacing: 1px; }
  .cover__rule {
    position: absolute; left: 60px; top: 560px;
    width: 400px; height: 2px; background: var(--rule);
  }
  .cover__ref {
    position: absolute; left: 60px; top: 574px;
    font-weight: 700; font-size: 22px; letter-spacing: 1px;
  }
  .cover__brand {
    position: absolute; left: 60px; top: 630px;
    text-align: left;
  }
  .cover__brand .brand__name { font-size: 54px; }
  .cover__brand .brand__url { font-size: 9px; }
</style>
</head>
<body>
  <main class="spread">
    <section class="page page--inside">
      <header class="brand">
        <div class="brand__name">OSB</div>
        <div class="brand__url">www.oakstonebrotherhood.com</div>
      </header>

      <div class="pillars">
        <div class="pillar">
          <h2 class="pillar__title">Obey God</h2>
          <p class="pillar__label">Our Purpose</p>
        </div>
        <span class="pillars__divider"></span>
        <div class="pillar">
          <h2 class="pillar__title">Love Others</h2>
          <p class="pillar__label">Our Mission</p>
        </div>
      </div>
      <p class="verse">Jesus replied: “Love the Lord your God with all your heart and with all your soul and with all your mind. This is the first and greatest commandment. And the second is like it: ‘Love your neighbor as yourself.’ All the Law and the Prophets hang on these two commandments.”</p>
      <p class="verse__ref">Matthew 22:37-40</p>

      <div class="vision">
        <h2 class="vision__title">Our Vision</h2>
        <p class="vision__label">Develop God Fearing Men Globally</p>
      </div>
      <p class="verse">Then Jesus came to them and said, “All authority in heaven and on earth has been given to me. Therefore go and make disciples of all nations, baptizing them in the name of the Father and of the Son and of the Holy Spirit, and teaching them to obey everything I have commanded you. And surely I am with you always, to the very end of the age.”</p>
      <p class="verse__ref">Matthew 28:18-20</p>
    </section>

    <section class="page page--cover">
      <div class="cover__scene" role="img" aria-label="Photograph of Jesus reaching out on a sunlit shore with disciples walking from the surf and boats on the water at sunset"></div>
      <h1 class="cover__title">
        <span class="cover__title-top">TEACHINGS</span>
        <span class="cover__title-of">OF </span><span class="cover__title-main">JESUS</span>
      </h1>
      <span class="cover__rule"></span>
      <p class="cover__ref">Matthew 28:18-20</p>
      <div class="brand cover__brand">
        <div class="brand__name">OSB</div>
        <div class="brand__url">www.oakstonebrotherhood.com</div>
      </div>
    </section>
  </main>
</body>
</html>
```